New Business Card Design Project

Updated business card design. I am moving towards more coaching of, for the most part women, who are searching for more in their lives. I am an intuitive healer, homeopath and nutritionist but also an author and motivational speaker. Int the past I have included my photo on the card but that is not essential. My book is called the Brilliance of Saffron - Reclaiming the Shade of Your Spirit so my colours are typically magenta.
Target Market(s)
Women - 35 - 60 considering improving their health. However, I am also a professional speaker with a target audience including corporate and conferences.
Industry/Entity Type
Health And Wellness
Contact Information for Business Card
Delia Tranmoor, Hom, RHN, BA
www.deliatranmoor.example
delia@deliatranmoor.example
555-203-7914
Facebook, instagram and twitter logos
Look and feel
Each slider illustrates characteristics of the customer's brand and the style your logo design should communicate.

```html
<!DOCTYPE html>
<html lang="en">
<head>
<meta charset="utf-8">
<title>Delia Tranmoor – Business Card</title>
<link href="https://fonts.googleapis.com/css2?family=Alice&family=Josefin+Sans:wght@300;400&display=swap" rel="stylesheet">
<style>
  :root {
    --backdrop: #2a2a2b;
    --card-dark: #1e1e1f;
    --card-light: #efefef;
    --ink: #231f20;
    --ink-soft: #3a3536;
    --paper-text: #f2f2f2;
    --magenta: #d62d6c;
    --magenta-band: #d33a72;
    --pattern-tone: #e4e4e4;
  }
  * { box-sizing: border-box; margin: 0; padding: 0; }
  html, body { width: 1200px; height: 794px; overflow: hidden; }
  body { background: var(--backdrop); position: relative; font-family: "Josefin Sans", sans-serif; }

  .card { position: absolute; border-radius: 12px; overflow: hidden; }

  /* Front */
  .card-front { left: 228px; top: 270px; width: 450px; height: 272px; background: var(--card-dark); box-shadow: 0 2px 6px rgba(0,0,0,.5); }
  .front-logo { position: absolute; left: 0; right: 0; top: 100px; display: flex; justify-content: center; align-items: center; gap: 12px; }
  .brand-dot { width: 40px; height: 40px; border-radius: 50%; background: var(--magenta); flex: none; }
  .front-name { font-family: "Alice", serif; font-size: 44px; color: var(--paper-text); line-height: 1; }
  .front-tagline { position: absolute; left: 0; right: 0; top: 154px; text-align: center; font-weight: 300; font-size: 17px; color: var(--paper-text); letter-spacing: .3px; }
  .bullet { color: var(--magenta); }

  /* Back */
  .card-back { left: 700px; top: 172px; width: 272px; height: 450px; background: var(--card-light); box-shadow: 0 2px 6px rgba(0,0,0,.5); }
  .pattern-area { position: absolute; left: 30px; top: 190px; width: 220px; height: 220px; border-radius: 50%; background: radial-gradient(circle, var(--pattern-tone) 0%, var(--card-light) 70%); }
  .back-logo { position: absolute; left: 0; right: 0; top: 42px; text-align: center; }
  .back-name { font-family: "Alice", serif; font-size: 40px; line-height: 40px; color: var(--ink); }
  .back-name .line { display: block; }
  .back-name .brand-dot { display: inline-block; width: 30px; height: 30px; vertical-align: middle; margin-left: 6px; }
  .credentials { position: absolute; left: 0; right: 0; top: 159px; text-align: center; font-size: 13px; color: var(--ink-soft); }
  .divider { position: absolute; left: 56px; right: 56px; top: 219px; display: flex; align-items: center; gap: 6px; }
  .divider .rule { flex: 1; height: 2px; background: var(--magenta); }
  .divider .icons { display: flex; gap: 4px; }
  .contact { position: absolute; left: 0; right: 0; top: 253px; text-align: center; font-family: "Alice", serif; font-size: 14px; line-height: 19px; color: var(--ink); }
  .follow { position: absolute; left: 0; right: 0; top: 347px; text-align: center; font-family: "Alice", serif; font-size: 14px; color: var(--ink); }
  .social { position: absolute; left: 0; right: 0; top: 372px; display: flex; justify-content: center; gap: 5px; }
  .social span { width: 19px; height: 19px; border-radius: 50%; background: var(--magenta); }
  .band { position: absolute; left: 0; right: 0; bottom: 0; height: 30px; background: var(--magenta-band); color: #fff; text-align: center; font-weight: 300; font-size: 13px; line-height: 32px; }
</style>
</head>
<body>
  <section class="card card-front">
    <div class="front-logo">
      <span class="brand-dot"></span>
      <span class="front-name">Delia Tranmoor</span>
    </div>
    <p class="front-tagline"><span class="bullet">•</span> wellness renegade <span class="bullet">•</span></p>
  </section>

  <section class="card card-back">
    <div class="pattern-area" role="img" aria-label="Faint swirl pattern behind contact details"></div>
    <div class="back-logo">
      <p class="back-name"><span class="line">Delia<span class="brand-dot"></span></span><span class="line">Tranmoor</span></p>
    </div>
    <p class="credentials">Hom, RHN, BA</p>
    <div class="divider">
      <span class="rule"></span>
      <span class="icons">
        <svg width="19" height="19" viewBox="0 0 20 20" aria-label="Phone"><circle cx="10" cy="10" r="9" fill="#fff" stroke="#d62d6c" stroke-width="1.5"/><path d="M6 8q4-3 8 0l-1 2h-6z M7 11h6v3h-6z" fill="#d62d6c"/></svg>
        <svg width="19" height="19" viewBox="0 0 20 20" aria-label="Email"><circle cx="10" cy="10" r="9" fill="#fff" stroke="#d62d6c" stroke-width="1.5"/><rect x="5" y="6.5" width="10" height="7" fill="#d62d6c"/><path d="M5 6.5l5 4 5-4" stroke="#fff" fill="none"/></svg>
        <svg width="19" height="19" viewBox="0 0 20 20" aria-label="Website"><circle cx="10" cy="10" r="9" fill="#fff" stroke="#d62d6c" stroke-width="1.5"/><circle cx="10" cy="10" r="5" fill="none" stroke="#d62d6c"/><path d="M5 10h10M10 5v10M10 5q-3 5 0 10M10 5q3 5 0 10" stroke="#d62d6c" fill="none" stroke-width=".8"/></svg>
      </span>
      <span class="rule"></span>
    </div>
    <div class="contact">
      <p>555-203-7914</p>
      <p>www.deliatranmoor.example</p>
      <p>delia@deliatranmoor.example</p>
    </div>
    <p class="follow">Follow us on</p>
    <div class="social">
      <span role="img" aria-label="Social network profile"></span>
      <span role="img" aria-label="Social network profile"></span>
      <span role="img" aria-label="Social network profile"></span>
    </div>
    <p class="band">• wellness renegade •</p>
  </section>
</body>
</html>
```